Animal Eye Clinic needs a Business card

We are a new veterinary ophthalmology practice (Tessaly Animal Eye Care) and we need a business card designed. We only see animal eyes - we are not a regular veterinary clinic. We already have a logo. We are looking for a professional, good looking business card to hand out to our clients. We are looking for something simple but professional and contemporary. Our logo is likely the only picture/graphic that needs to be on the card.
Updates

Contact Information for Business Card

Marisol Dunkley, BSc, DVM, MSc, DipACVO
Veterinary Ophthalmologist

Phone: 250.418.3097
Email: tessalyanimaleyecare@mailbrook.net
Website: tessalyanimaleyecare.net
Address: 1840 Pellworth Rd
Kelowna, BC, V4T 8M3

Colors

Designer to choose colors to be used in the design.

Requirements
Must have
• Our logo (attached)

```html
<!DOCTYPE html>
<html lang="en">
<head>
<meta charset="utf-8">
<title>Tessaly Animal Eye Care — Business Card</title>
<link rel="stylesheet" href="https://fonts.googleapis.com/css2?family=Open+Sans:wght@400;600;700&display=swap">
<style>
  :root {
    --backdrop: #0f8fab;
    --card-white: #f1f1f1;
    --brand-teal: #1b8f9e;
    --panel-blue-start: #069dc6;
    --panel-blue-end: #2cb4d5;
    --text-on-blue: #ffffff;
    --icon-disc: #ffffff;
    --icon-ink: #14a4c9;
  }
  * { box-sizing: border-box; margin: 0; padding: 0; }
  html, body { width: 1200px; height: 900px; overflow: hidden; }
  body {
    background: var(--backdrop);
    font-family: "Open Sans", Arial, sans-serif;
    position: relative;
  }
  .card {
    position: absolute;
    left: 354px;
    width: 491px;
    height: 317px;
    background: var(--card-white);
    box-shadow: 0 8px 18px rgba(0, 20, 40, 0.35);
    overflow: hidden;
  }
  .card--front { top: 93px; }
  .card--back { top: 457px; }

  /* Front */
  .front-brand {
    position: absolute;
    left: 40px;
    top: 118px;
    display: flex;
    align-items: center;
    gap: 22px;
  }
  .front-brand__dot {
    width: 62px;
    height: 62px;
    border-radius: 50%;
    background: var(--brand-teal);
    flex: none;
  }
  .front-brand__name {
    color: var(--brand-teal);
    font-weight: 700;
    line-height: 1.05;
  }
  .front-brand__name .line-1 {
    display: block;
    font-size: 22px;
    letter-spacing: 13px;
  }
  .front-brand__name .line-2 {
    display: block;
    font-size: 31px;
    letter-spacing: -0.5px;
  }

  /* Back */
  .back-panel {
    position: absolute;
    inset: 0;
    width: 491px;
    height: 317px;
  }
  .back-brand {
    position: absolute;
    left: 16px;
    top: 140px;
    color: var(--brand-teal);
    font-weight: 700;
    line-height: 1.1;
  }
  .back-brand .line-1 {
    display: block;
    font-size: 13px;
    letter-spacing: 8px;
  }
  .back-brand .line-2 {
    display: block;
    font-size: 18px;
    letter-spacing: -0.3px;
  }
  .person {
    position: absolute;
    left: 243px;
    top: 32px;
    color: var(--text-on-blue);
  }
  .person__name {
    font-size: 20px;
    font-weight: 700;
    letter-spacing: 3.5px;
    line-height: 1.1;
  }
  .person__credentials,
  .person__role {
    font-size: 12.5px;
    letter-spacing: 2px;
    line-height: 1.35;
  }
  .contact {
    position: absolute;
    display: flex;
    align-items: center;
    color: var(--text-on-blue);
    font-size: 13.5px;
    font-weight: 600;
    line-height: 1.2;
  }
  .contact__icon {
    width: 30px;
    height: 30px;
    flex: none;
  }
  .contact--phone { left: 233px; top: 113px; gap: 16px; }
  .contact--web   { left: 226px; top: 159px; gap: 15px; }
  .contact--address { left: 211px; top: 205px; gap: 15px; }
  .contact--mail  { left: 187px; top: 251px; gap: 14px; font-size: 12.5px; }
</style>
</head>
<body>

  <section class="card card--front" aria-label="Business card front">
    <div class="front-brand">
      <span class="front-brand__dot"></span>
      <p class="front-brand__name">
        <span class="line-1">TESSALY</span>
        <span class="line-2">ANIMAL EYE CARE</span>
      </p>
    </div>
  </section>

  <section class="card card--back" aria-label="Business card back">
    <svg class="back-panel" viewBox="0 0 491 317" aria-hidden="true">
      <defs>
        <linearGradient id="panelGradient" x1="0" y1="0" x2="1" y2="1">
          <stop offset="0" stop-color="var(--panel-blue-start)"/>
          <stop offset="1" stop-color="var(--panel-blue-end)"/>
        </linearGradient>
      </defs>
      <path d="M190 0 C 238 78, 232 222, 136 317 L491 317 L491 0 Z" fill="url(#panelGradient)"/>
    </svg>

    <p class="back-brand">
      <span class="line-1">TESSALY</span>
      <span class="line-2">ANIMAL EYE CARE</span>
    </p>

    <div class="person">
      <h1 class="person__name">Marisol Dunkley</h1>
      <p class="person__credentials">BSc, DVM, MSc, DipACVO</p>
      <p class="person__role">Veterinary Ophthalmologist</p>
    </div>

    <div class="contact contact--phone">
      <svg class="contact__icon" viewBox="0 0 30 30" aria-hidden="true">
        <circle cx="15" cy="15" r="15" fill="var(--icon-disc)"/>
        <path d="M10.2 8.2c.6-.5 1.4-.4 1.8.2l1.6 2.3c.4.6.3 1.3-.2 1.7l-.9.8c.7 1.6 2 2.9 3.6 3.7l.8-.9c.4-.5 1.2-.6 1.7-.2l2.3 1.6c.6.4.7 1.2.2 1.8l-1 1.2c-.6.7-1.6 1-2.5.7-4.2-1.4-7.5-4.7-8.9-8.9-.3-.9 0-1.9.7-2.5z" fill="var(--icon-ink)"/>
      </svg>
      <span>250.418.3097</span>
    </div>

    <div class="contact contact--web">
      <svg class="contact__icon" viewBox="0 0 30 30" aria-hidden="true">
        <circle cx="15" cy="15" r="15" fill="var(--icon-disc)"/>
        <g fill="none" stroke="var(--icon-ink)" stroke-width="1.6">
          <circle cx="15" cy="15" r="8"/>
          <ellipse cx="15" cy="15" rx="3.5" ry="8"/>
          <line x1="7" y1="15" x2="23" y2="15"/>
          <line x1="8.3" y1="11" x2="21.7" y2="11"/>
          <line x1="8.3" y1="19" x2="21.7" y2="19"/>
        </g>
      </svg>
      <span>tessalyanimaleyecare.net</span>
    </div>

    <div class="contact contact--address">
      <svg class="contact__icon" viewBox="0 0 30 30" aria-hidden="true">
        <circle cx="15" cy="15" r="15" fill="var(--icon-disc)"/>
        <path d="M15 7a5.5 5.5 0 0 0-5.5 5.5c0 4 5.5 10.5 5.5 10.5s5.5-6.5 5.5-10.5A5.5 5.5 0 0 0 15 7zm0 7.7a2.2 2.2 0 1 1 0-4.4 2.2 2.2 0 0 1 0 4.4z" fill="var(--icon-ink)"/>
      </svg>
      <span>1840 Pellworth Rd<br>Kelowna, BC, V4T 8M3</span>
    </div>

    <div class="contact contact--mail">
      <svg class="contact__icon" viewBox="0 0 30 30" aria-hidden="true">
        <circle cx="15" cy="15" r="15" fill="var(--icon-disc)"/>
        <rect x="8.5" y="10" width="13" height="10" rx="1.5" fill="var(--icon-ink)"/>
        <path d="M9 11l6 4.5 6-4.5" fill="none" stroke="var(--icon-disc)" stroke-width="1.3"/>
      </svg>
      <span>tessalyanimaleyecare@mailbrook.net</span>
    </div>
  </section>

</body>
</html>
```